"KTR Community Supports" Business Card Design

We are a not for profit disability service that has recently changed its logo and trading name and is in the process of "rebranding".We provide employment, training and accommodation to people with disabilities. We find our new logo fresh and inspiring and would like our new business cards to reflect the same feeling. Our marketing line is "Growth, Opportunity, Empowerment".

Target Market(s)

People with disabilities and their families, carers, support network

Industry/Entity Type

Business

Contact Information for Business Card

Requirements
Must have
• Our logo; space for the above listed information requirements

```html
<!DOCTYPE html>
<html lang="en">
<head>
<meta charset="utf-8">
<title>KTR Community Supports – Business Card</title>
<link rel="stylesheet" href="https://fonts.googleapis.com/css2?family=Open+Sans:wght@400;600;700&display=swap">
<style>
  :root {
    --page-bg: #e8e5e1;
    --card-white: #ffffff;
    --brand-blue: #1a5ea8;
    --brand-navy: #143f7d;
    --brand-deep: #0d3470;
    --brand-green: #5f9a2e;
    --text-dark: #2a2a2a;
    --back-centre: #0b78bf;
    --back-edge: #0c3574;
  }
  * { box-sizing: border-box; margin: 0; padding: 0; }
  html, body { width: 1200px; height: 1000px; overflow: hidden; }
  body {
    background: var(--page-bg);
    font-family: "Open Sans", Arial, sans-serif;
    position: relative;
  }
  .card {
    position: absolute;
    left: 265px;
    width: 665px;
    height: 397px;
    border-radius: 22px;
    overflow: hidden;
    box-shadow: 0 6px 18px rgba(0,0,0,0.25);
  }
  .card--front { top: 73px; background: var(--card-white); }
  .card--back {
    top: 532px;
    background: radial-gradient(ellipse at 45% 45%, var(--back-centre) 0%, #0a5a9e 45%, var(--back-edge) 100%);
  }
  .card__decor { position: absolute; inset: 0; width: 100%; height: 100%; }

  .contact { position: absolute; left: 26px; top: 166px; color: var(--text-dark); }
  .contact__name { font-size: 17px; font-weight: 700; color: var(--brand-blue); line-height: 22px; }
  .contact__role { font-size: 15px; line-height: 20px; }
  .contact__address { font-size: 15px; line-height: 20px; margin-top: 19px; }
  .contact__list { list-style: none; margin-top: 12px; font-size: 15px; line-height: 19.5px; }
  .contact__list li { display: flex; align-items: center; gap: 6px; }
  .contact__list svg { width: 13px; height: 13px; fill: var(--brand-navy); flex: none; }

  .brand {
    position: absolute;
    display: flex;
    align-items: center;
    gap: 14px;
  }
  .brand__dot { border-radius: 50%; flex: none; }
  .brand__name { font-weight: 600; line-height: 1.05; }

  .brand--front { right: 26px; top: 112px; }
  .brand--front .brand__dot { width: 46px; height: 46px; background: var(--brand-green); }
  .brand--front .brand__name { font-size: 34px; color: var(--brand-navy); text-align: right; }

  .brand--back { left: 50%; top: 50%; transform: translate(-50%, -50%); }
  .brand--back .brand__dot { width: 60px; height: 60px; background: #ffffff; }
  .brand--back .brand__name { font-size: 42px; color: #ffffff; }
</style>
</head>
<body>

<section class="card card--front" aria-label="Business card front">
  <svg class="card__decor" viewBox="0 0 665 397" aria-hidden="true">
    <path d="M0 0 H170 Q45 45 0 150 Z" fill="var(--brand-blue)"/>
    <path d="M150 18 Q60 50 22 140" fill="none" stroke="var(--brand-green)" stroke-width="3"/>
    <path d="M665 235 Q620 360 490 397 H665 Z" fill="var(--brand-blue)"/>
    <path d="M650 262 Q610 335 520 362" fill="none" stroke="var(--brand-green)" stroke-width="3"/>
  </svg>

  <div class="brand brand--front">
    <span class="brand__dot"></span>
    <span class="brand__name">KTR Community<br>Supports</span>
  </div>

  <div class="contact">
    <p class="contact__name">Daniel Hartley</p>
    <p class="contact__role">Markerting Manager</p>
    <p class="contact__address">14 Wattle Grove Road<br>Ashford VIC 3790</p>
    <ul class="contact__list">
      <li><svg viewBox="0 0 16 16"><path d="M4 1l3 3-2 2c1 2 3 4 5 5l2-2 3 3-2 3C7 15 1 9 1 3z"/></svg>999 999 9999</li>
      <li><svg viewBox="0 0 16 16"><path d="M1 5c0-2 14-2 14 0v2h-4V5H5v2H1zM3 8h10l2 7H1zM6 10h4v3H6z"/></svg>999 999 9999</li>
      <li><svg viewBox="0 0 16 16"><path d="M4 1h8v4H4zM1 6h14v6h-3V9H4v3H1zM5 10h6v5H5z"/></svg>999 999 9999</li>
      <li><svg viewBox="0 0 16 16"><path d="M1 3h14v10H1zM2 4l6 5 6-5v1l-6 5-6-5z" fill-rule="evenodd"/></svg>info@ktrcomsupports.com</li>
      <li><svg viewBox="0 0 16 16"><circle cx="8" cy="8" r="7" fill="none" stroke="var(--brand-navy)" stroke-width="1.4"/><path d="M1 8h14M8 1c-4 4-4 10 0 14M8 1c4 4 4 10 0 14" fill="none" stroke="var(--brand-navy)" stroke-width="1.2"/></svg>www.ktrcomsupports.com</li>
    </ul>
  </div>
</section>

<section class="card card--back" aria-label="Business card back">
  <div class="brand brand--back">
    <span class="brand__dot"></span>
    <span class="brand__name">KTR Community Supports</span>
  </div>
</section>

</body>
</html>
```